Brontaro Web Site

Redesigned web site for Brontaro Ltd (www.brontaro-example.co.uk). This is to feature new logo (attached). Brontaro Ltd is a company which specialises in Geographic Information Systems and Geographic data - we call ourselves GIS Data Specialists. We are looking for something which conveys our professionalism and our experience. There will be more pages than on the current Brontaro website. There will be: Home, Data Migration, Data Cleansing & Validation, Data Analysis, Data Maintenance, Data Quality and an About Us page. All these should be accessible from each page on the website.
Updates
I didn't really think to say that the content of the web site is going to change from the current one we have. There will be more pages than on the current one. They will be: Home, Data Migration, Data Cleansing & Validation, Data Analysis, Data Maintenance, Data Quality and an About Us page. All these should be accessible from each page on the website. I didn't really think through the fact that the number of pages / areas to access can influence the layout of the site, sorry.
Target Market(s)
Utility Companies (e.g. telecommunications providers, energy companies), local government.
Industry/Entity Type
It Company
Look and feel

```html
<!DOCTYPE html>
<html lang="en">
<head>
<meta charset="utf-8">
<title>Brontaro Web Site</title>
<link rel="stylesheet" href="https://fonts.googleapis.com/css2?family=Noto+Sans:wght@400;700&display=swap">
<style>
:root{
  --black:#000;
  --teal:#5fb3bb;
  --teal-light:#8ed3d9;
  --nav-text:#8fdbe3;
  --ink:#111;
  --link:#1e5a60;
  --grey:#939598;
  --panel:#f4f4f4;
  --rule:#bbb;
  --white:#fff;
}
*{box-sizing:border-box;margin:0;padding:0}
html,body{width:1200px;height:800px;overflow:hidden}
body{position:relative;background:var(--white);font-family:"Noto Sans",Verdana,sans-serif;color:var(--ink)}
.header-band{position:absolute;left:0;top:0;width:1200px;height:106px;background:var(--black)}
.accent-band{position:absolute;left:0;top:106px;width:1200px;height:76px;background:linear-gradient(var(--teal-light),#9adade)}
.world-map{position:absolute;left:410px;top:0;width:660px;height:182px;
  background:radial-gradient(ellipse at 60% 30%,rgba(255,255,255,.22),rgba(255,255,255,0) 65%)}
.social{position:absolute;top:17px;left:888px;display:flex;gap:11px}
.social span{width:24px;height:24px;border-radius:50%;background:var(--teal);opacity:.85}
.social span:first-child{opacity:.4}
.utility{position:absolute;top:79px;left:1000px;display:flex;gap:7px}
.brand-card{position:absolute;left:149px;top:0;width:261px;height:132px;background:var(--white);border-radius:0 0 8px 8px;box-shadow:0 4px 10px rgba(0,0,0,.2);display:flex;align-items:center;padding-left:24px;gap:12px}
.brand-card .dot{width:36px;height:36px;border-radius:50%;background:var(--teal)}
.brand-card .name{font-size:32px;color:#6d6e71;font-weight:400}
.main-nav{position:absolute;left:149px;top:152px;width:261px;height:364px;padding-top:4px;background:var(--black);border-radius:8px;box-shadow:0 6px 14px rgba(0,0,0,.25);list-style:none}
.main-nav li{height:51px;display:flex;align-items:center;padding-left:24px;border-bottom:1px dotted #444;font-size:13px;font-weight:700;color:var(--nav-text);gap:12px}
.main-nav li:last-child{border-bottom:0}
.terms{position:absolute;left:149px;top:532px;width:261px;height:50px;padding-bottom:3px;background:var(--grey);border-radius:8px;display:flex;align-items:center;padding-left:48px}
.terms span{color:var(--white);font-size:13px;font-weight:700;border-bottom:1px dotted var(--white)}
.content{position:absolute;left:439px;top:152px;width:611px}
.content h1{font-size:18px;font-weight:400;letter-spacing:.3px;margin-bottom:19px}
.intro{font-size:13px;line-height:24px}
.columns{display:flex;margin-top:11px}
.col h2{font-size:13px;font-weight:700;border-bottom:1px solid var(--rule);padding-bottom:2px;margin-bottom:7px}
.col p{font-size:13px;line-height:24px;white-space:nowrap}
.col.c1{width:180px;margin-right:17px}
.col.c2{width:206px;margin-right:13px}
.col.c3{width:195px}
.callout{position:absolute;left:439px;top:633px;width:611px;height:72px;background:var(--panel);border-top:1px dotted #999;border-bottom:1px dotted #999;padding:7px 13px;font-size:13px;line-height:24px}
.callout b{color:var(--link)}
.footer{position:absolute;left:149px;top:734px;width:901px;height:66px;background:var(--teal);border-top:6px solid var(--black);border-radius:8px 8px 0 0;text-align:right;padding:11px 21px;font-size:13px}
</style>
</head>
<body>
<div class="header-band"></div>
<div class="accent-band"></div>
<div class="world-map" role="img" aria-label="Faint world map backdrop"></div>
<div class="social"><span></span><span></span><span></span><span></span><span></span></div>
<div class="utility">
  <svg width="11" height="10" viewBox="0 0 11 10"><path d="M1 5 5.5 1 10 5M2.5 4v5h6V4" fill="none" stroke="#8fdbe3"/></svg>
  <svg width="11" height="10" viewBox="0 0 11 10"><rect x="4" y="0.5" width="3" height="2.5" fill="none" stroke="#8fdbe3"/><path d="M5.5 3v2M1.5 7V5h8v2" fill="none" stroke="#8fdbe3"/><rect x="0.5" y="7" width="2.5" height="2.5" fill="#8fdbe3"/><rect x="8" y="7" width="2.5" height="2.5" fill="#8fdbe3"/></svg>
  <svg width="12" height="9" viewBox="0 0 12 9"><rect x="0.5" y="0.5" width="11" height="8" fill="none" stroke="#8fdbe3"/><path d="M.5.5 6 5l5.5-4.5" fill="none" stroke="#8fdbe3"/></svg>
</div>
<div class="brand-card"><span class="dot"></span><span class="name">Brontaro</span></div>
<ul class="main-nav">
  <li><svg width="12" height="10" viewBox="0 0 12 10"><path d="M1 1l4 4-4 4M6 1l4 4-4 4" fill="none" stroke="#bbb"/></svg>Home</li>
  <li><svg width="12" height="10" viewBox="0 0 12 10"><path d="M1 1l4 4-4 4M6 1l4 4-4 4" fill="none" stroke="#bbb"/></svg>Data Migration</li>
  <li><svg width="12" height="10" viewBox="0 0 12 10"><path d="M1 1l4 4-4 4M6 1l4 4-4 4" fill="none" stroke="#bbb"/></svg>Data Cleansing &amp; Validation</li>
  <li><svg width="12" height="10" viewBox="0 0 12 10"><path d="M1 1l4 4-4 4M6 1l4 4-4 4" fill="none" stroke="#bbb"/></svg>Data Analysis</li>
  <li><svg width="12" height="10" viewBox="0 0 12 10"><path d="M1 1l4 4-4 4M6 1l4 4-4 4" fill="none" stroke="#bbb"/></svg>Data Maintenance</li>
  <li><svg width="12" height="10" viewBox="0 0 12 10"><path d="M1 1l4 4-4 4M6 1l4 4-4 4" fill="none" stroke="#bbb"/></svg>Data Quality</li>
  <li><svg width="12" height="10" viewBox="0 0 12 10"><path d="M1 1l4 4-4 4M6 1l4 4-4 4" fill="none" stroke="#bbb"/></svg>About Us</li>
</ul>
<div class="terms"><span>Terms and Conditions</span></div>
<main class="content">
  <h1>WELCOME TO BRONTARO</h1>
  <p class="intro">Brontaro was founded in 1994 by a group of geospatial software engineers that recognised the significant value that data, and the systems used to store and analyse this data, could bring to business.</p>
  <div class="columns">
    <section class="col c1"><h2>Our Customers:</h2><p>We have worked with over<br>200 companies in a myriad<br>of market sectors - from<br>utilities, local and central<br>government, oil and gas, to<br>many spheres of the marine<br>industry.</p></section>
    <section class="col c2"><h2>Our Pedigree:</h2><p>We provide a vast bank of<br>knowledge and experience to<br>offer an all encompassing<br>service. This ensures that you,<br>as a customer, reap the<br>maximum benefits from your<br>data and systems through utilis-<br>ing a combination of our skilled<br>consultants, analysts and devel-<br>opers that will work with you<br>and your requirements to help<br>achieve your business objec-<br>tives.</p></section>
    <section class="col c3"><h2>Our People:</h2><p>We have a wide ranging skill<br>set including QUANTA 2 quali-<br>fied Project Managers, fully<br>qualified Software Developers<br>and Experienced Data Consul-<br>tants.</p></section>
  </div>
</main>
<div class="callout">We can be on hand to help with any or all parts of your data projects via: <b>Data Consultancy</b>, <b>System Consultancy</b>, <b>Software Development</b>.</div>
<footer class="footer">© 2010 Brontaro Ltd. Registered in Scotland No. 284317</footer>
</body>
</html>
```